Coffee bag and coffee beer revamp

We need a coffee bag design where we can print two stickers and they fit nicely on the bag. this is an example of 500gr bag. We will also need 250gr and 1kilo versions.

One the logo attached and the other the coffee description details attached.
This should sit nicely on the white bag example attached.
One is also a photo of what we have but it needed some work to make sure dimensions are good and its clear.
Example: attached of text and these will be variable values that we need the label to edit and they should be different colour labels - we have 6 types of coffee.

<COFFEE TYPE> example House BLEND
<DATE ROASTED> 17/03/23
Text always the same -- "Consume within 12 months"

I have also attache the font and original files. There can be some colour added.

Other types of coffee

SIDAMO
GUATEMALA
SANTOS
COSTA RICA
SUPREMO
DECAF

The beer is just the logo and text "Bendula Cold Brew Coffee" label with the date and logo.

Target Market(s)

coffee lovers

Industry/Entity Type

food

Font styles to use
Other font styles liked:
• i will upload the fonts

Colors
EB3D1F
EC4F4E
F09395
F8D3D4
FCEDEE

Requirements
Nice to have
• can try alternative colour? even just for labels

```html
<!DOCTYPE html>
<html lang="en">
<head>
<meta charset="utf-8">
<title>Bendula Coffee – House Blend bag label</title>
<link rel="stylesheet" href="https://fonts.googleapis.com/css2?family=Archivo+Black&family=Roboto:wght@400;500;700&family=Roboto+Mono:wght@400&family=Open+Sans:wght@400&display=swap">
<style>
  :root{
    --brand-red:#BF1E2E;
    --ink:#333333;
    --dieline:#29ABE2;
    --zip-grey:#E6E6E6;
    --paper:#FFFFFF;
    --badge-light:#F8D3D4;
  }
  *{margin:0;padding:0;box-sizing:border-box;}
  html,body{width:1200px;height:2359px;overflow:hidden;background:var(--paper);}
  .canvas{position:relative;width:1200px;height:2359px;background:var(--paper);font-family:"Roboto",Arial,sans-serif;color:var(--ink);}

  .dieline{position:absolute;inset:0;width:1200px;height:2359px;}
  .dim-label{font-family:"Open Sans",Arial,sans-serif;font-size:14px;fill:var(--dieline);}

  .zip-stripe{position:absolute;left:303px;width:604px;background:var(--zip-grey);}

  .blend-band{position:absolute;left:303px;top:258px;width:604px;height:138px;background:var(--brand-red);
    display:flex;align-items:center;justify-content:center;}
  .blend-name{font-family:"Archivo Black",Arial,sans-serif;color:var(--paper);font-size:40px;letter-spacing:0.36em;margin-right:-0.36em;}

  .front-badge{position:absolute;left:437px;top:421px;width:336px;height:555px;border-radius:168px 168px 150px 150px;
    background:radial-gradient(circle at 50% 35%, var(--badge-light) 0%, #E59A9F 35%, var(--brand-red) 75%);}
  .front-brand{position:absolute;left:437px;top:736px;width:336px;text-align:center;
    font-family:"Archivo Black",Arial,sans-serif;font-size:40px;color:var(--paper);letter-spacing:0.04em;}

  /* back panel, printed upside down */
  .back-panel{position:absolute;left:365px;top:1443px;width:478px;height:678px;transform:rotate(180deg);}
  .back-panel > *{position:absolute;left:0;width:478px;}

  .web-bar{top:0;height:40px;background:var(--brand-red);color:var(--paper);display:flex;align-items:center;justify-content:center;
    font-family:"Archivo Black",Arial,sans-serif;font-size:15px;letter-spacing:0.42em;}
  .handcrafted{top:52px;height:40px;display:flex;justify-content:space-between;align-items:center;
    font-family:"Archivo Black",Arial,sans-serif;font-size:40px;line-height:1;color:var(--ink);}
  .rule{top:104px;height:4px;background:var(--ink);}
  .story{font-size:10.2px;line-height:1.3;color:var(--brand-red);text-align:center;}
  .story-nl{top:118px;}
  .story-fr{top:200px;}
  .story-en{top:287px;}

  .address-bar{top:360px;height:26px;border-bottom:3px solid var(--ink);display:flex;justify-content:space-between;align-items:stretch;
    font-size:11px;letter-spacing:0.04em;text-transform:uppercase;}
  .address-bar span{display:flex;align-items:center;}
  .address-street{background:var(--ink);color:var(--paper);padding:0 14px;}
  .contact-line{top:396px;font-size:11.5px;letter-spacing:0.03em;text-align:center;text-transform:uppercase;}

  .date-box{background:var(--brand-red);border-radius:9px;padding:0 4px 4px;}
  .date-box-label{height:24px;display:flex;align-items:center;justify-content:center;color:var(--paper);
    font-family:"Archivo Black",Arial,sans-serif;font-size:11px;letter-spacing:0.14em;}
  .date-box-value{height:22px;background:var(--paper);display:flex;align-items:center;justify-content:center;
    font-family:"Roboto Mono",monospace;font-size:12.5px;color:var(--ink);}
  .roasted-box{top:431px;width:388px;}
  .best-before{top:495px;width:254px;}

  .caffeine{top:573px;width:250px;font-size:9.5px;line-height:1.9;color:var(--ink);}
  .back-brand{top:500px;left:270px;width:208px;height:100px;display:flex;align-items:center;justify-content:center;
    font-family:"Archivo Black",Arial,sans-serif;font-size:38px;color:var(--ink);}
  .net-weight{top:656px;left:120px;width:238px;text-align:center;font-family:"Archivo Black",Arial,sans-serif;font-size:18px;
    letter-spacing:0.3em;color:var(--brand-red);}
</style>
</head>
<body>
<main class="canvas">

  <svg class="dieline" viewBox="0 0 1200 2359" aria-hidden="true">
    <g fill="none" stroke="var(--dieline)" stroke-width="1">
      <rect x="303" y="89" width="604" height="2233" rx="10"/>
      <line x1="322" y1="89" x2="322" y2="2322"/>
      <line x1="887" y1="89" x2="887" y2="2322"/>
      <line x1="303" y1="1005" x2="907" y2="1005"/>
      <line x1="303" y1="1026" x2="907" y2="1026"/>
      <line x1="303" y1="1367" x2="907" y2="1367"/>
      <line x1="303" y1="1386" x2="907" y2="1386"/>
      <path d="M303 158 a3 3 0 0 1 0 6 M907 158 a3 3 0 0 0 0 6 M303 2252 a3 3 0 0 1 0 6 M907 2252 a3 3 0 0 0 0 6"/>
      <!-- overall width -->
      <line x1="303" y1="55" x2="907" y2="55"/>
      <path d="M309 52 l-6 3 l6 3 M901 52 l6 3 l-6 3"/>
      <!-- side margins -->
      <line x1="303" y1="80" x2="322" y2="80"/><line x1="887" y1="80" x2="907" y2="80"/>
      <!-- hang hole offset -->
      <line x1="916" y1="166" x2="916" y2="205"/>
      <!-- outer height -->
      <line x1="226" y1="89" x2="226" y2="2322"/>
      <path d="M221 89 h10 M221 1026 h10 M221 1386 h10 M221 2322 h10"/>
      <!-- top zip dims -->
      <line x1="275" y1="89" x2="275" y2="257"/>
      <path d="M270 89 h10 M270 205 h10 M270 257 h10"/>
      <!-- bottom zip dims -->
      <line x1="288" y1="2159" x2="288" y2="2322"/>
      <path d="M283 2159 h10 M283 2211 h10 M283 2322 h10"/>
    </g>
    <text class="dim-label" x="605" y="42" text-anchor="middle">5 7/8"</text>
    <text class="dim-label" x="309" y="76" text-anchor="middle">5mm</text>
    <text class="dim-label" x="892" y="74" text-anchor="middle">5mm</text>
    <text class="dim-label" x="922" y="188">10mm</text>
    <text class="dim-label" x="180" y="507" text-anchor="middle">9 1/8"</text>
    <text class="dim-label" x="186" y="1205" text-anchor="middle">3 1/2"</text>
    <text class="dim-label" x="246" y="150" text-anchor="middle">1 1/8"</text>
    <text class="dim-label" x="246" y="231" text-anchor="middle">1/2"</text>
    <text class="dim-label" x="256" y="2188" text-anchor="middle">1/2"</text>
    <text class="dim-label" x="256" y="2266" text-anchor="middle">1 1/8"</text>
  </svg>

  <div class="zip-stripe" style="top:205px;height:17px"></div>
  <div class="zip-stripe" style="top:227px;height:9px"></div>
  <div class="zip-stripe" style="top:241px;height:16px"></div>

  <section class="blend-band">
    <h1 class="blend-name">HOUSE BLEND</h1>
  </section>

  <div class="front-badge" role="img" aria-label="Vintage coffee badge illustration in red and white, with established date and 100% arabica band"></div>
  <p class="front-brand">BENDULA</p>

  <section class="back-panel">
    <div class="web-bar">WWW.BENDULACOFFEE.COM</div>
    <h2 class="handcrafted"><span>H</span><span>A</span><span>N</span><span>D</span><span>C</span><span>R</span><span>A</span><span>F</span><span>T</span><span>E</span><span>D</span></h2>
    <div class="rule"></div>
    <p class="story story-nl">In 2019 besloten Pieter en Lucas de oude familietraditie nieuw leven in te blazen. Gedurende vijf generaties stond Koffie Bendula, ook wel Koffie Verhoeven genoemd, garant voor kwalitatieve, artisanaal gebrande koffie. De blends zijn gebaseerd op het oude en beproefde recept van onze familie. Onze belangrijkste doelstelling is om u te laten genieten van een lekker kop koffie!</p>
    <p class="story story-fr">En 2019, Pieter et Lucas décident de continuer l'ancienne tradition familiale. Pendant cinq générations, Café Bendula, également connu sous le nom de Café Verhoeven, garantissait un café torréfié artisanalement et de grande qualité. Les mélanges sont basés sur la recette ancestrale et éprouvée de nos ancêtres. Notre objectif principal est de vous permettre de savourer une bonne tasse de café!</p>
    <p class="story story-en">In 2019 Pieter and Lucas decide to revive the old family tradition. For five generations long Coffee Bendula, also known as Coffee Verhoeven, was synonym for artisanally roasted premium quality coffee. The consistency of all our blends are based on the old family recipes. Our main purpose is to let you enjoy a nice cup of coffee!</p>
    <div class="address-bar">
      <span>Koffie Bendula</span>
      <span class="address-street">Lindenlaan 12</span>
      <span>9570 Heuvelbeek</span>
    </div>
    <p class="contact-line">hallo@koffiebendula.be - +32 50 12 34 56 &nbsp;- &nbsp;www.koffiebendula.be</p>
    <div class="date-box roasted-box">
      <div class="date-box-label">GEBRAND OP / TORREFIE LE / ROASTED ON</div>
      <div class="date-box-value">17/03/23</div>
    </div>
    <div class="date-box best-before">
      <div class="date-box-label">THT / DDM / BEST BEFORE</div>
      <div class="date-box-value">Consume within 12 months</div>
    </div>
    <div class="caffeine">
      <p>Cafeïnegehalte niet hoger dan 1,5%</p>
      <p>La teneur en caféinene ne dépasse pas 1,5%</p>
      <p>Max. cafeine content 1,5%</p>
    </div>
    <p class="back-brand">BENDULA</p>
    <p class="net-weight">250GR NETTO</p>
  </section>

</main>
</body>
</html>
```